Sci Fi/ Secret Agent Author needs website design!

My name is Tamsin Roark and I am an author. I require a site that can provide information about myself and my books and other works.

I would like it to have a Home, blog function, (about the) books/series section so people can visit another section and read about each individual book that's going to be released. A resources page, a Store, social media links and ability to load/embed videos from vidorra and other.

I write mild scifi/thriller/conspiracy/secret government type novels. -At the moment-. The series follows a strong female lead that is an agent with a secret organisation in a classified military installation.

The theme would be professional yet possibly show this element.

Target Market(s)

/military fiction/thriller/fantasy/Sci fi/ femme-fatal, readers. Mostly females, age 18-60
Novel readers

Number of Pages Required

5+ page

Requirements
Must have
• Would like designers to follow brief. :)
• My budget includes all the pages I will need;
• eg home, blog, resources, store, ability to pay with quidlo and Credit Cards
• , ability to have trailers from vidorra etc. Must have links to the social media mentioned in the brief.
Nice to have
• use of the colours I have suggested. electric/indigo purple, fuschia highlights , dark greys
• as I will possibly base branding for social media ETC on the look of your website design and colour scheme.
• Ability for trailer on front page??
Should not have
• Should not be too cluttered. (But I am open to all ideas)

```html
<!DOCTYPE html>
<html lang="en">
<head>
<meta charset="utf-8">
<title>Tamsin Roark – Conspiracy Novels</title>
<link href="https://fonts.googleapis.com/css2?family=Open+Sans:wght@400;600&family=Roboto+Slab:wght@700&family=Oswald:wght@500&display=swap" rel="stylesheet">
<style>
:root{
  --purple:#6a1bb0;
  --purple-deep:#472a57;
  --purple-band:#4a2d5e;
  --lavender:#d7b6f2;
  --ink:#222;
  --grey-text:#777;
  --light:#efefef;
  --footer:#262626;
  --white:#fff;
}
*{margin:0;padding:0;box-sizing:border-box}
html,body{width:1200px;height:2817px;overflow:hidden}
body{position:relative;font-family:"Open Sans",Arial,sans-serif;color:var(--ink);background:var(--white)}
.abs{position:absolute}
/* header */
.site-header{position:absolute;left:0;top:0;width:1200px;height:105px;background:var(--white)}
.brand{position:absolute;left:92px;top:34px;font-family:"Roboto Slab",Georgia,serif;font-weight:700;font-size:30px;color:var(--purple);letter-spacing:.5px}
.nav{position:absolute;top:36px;left:0;width:1200px;height:34px;font-size:16px}
.nav a{position:absolute;top:7px;color:var(--ink);text-decoration:none;line-height:20px}
.nav a.active{top:0;left:445px;width:77px;height:34px;line-height:34px;text-align:center;background:var(--purple);color:var(--white);border-radius:17px}
.cart{position:absolute;left:1076px;top:7px;font-size:15px;color:var(--ink);display:flex;align-items:center;gap:4px}
/* hero */
.hero{position:absolute;left:0;top:105px;width:1200px;height:581px;background:radial-gradient(ellipse at 35% 30%,#3a2a35 0%,#1a1418 45%,#0b0a0d 100%)}
.hero-title{position:absolute;left:92px;top:262px;font-size:52px;color:var(--lavender);line-height:60px;letter-spacing:1px}
.hero-sub{position:absolute;left:92px;top:326px;font-size:42px;color:var(--white);line-height:50px;font-weight:600}
.hero-tag{position:absolute;left:93px;top:380px;font-size:26px;color:var(--white)}
.book-cover{position:absolute;left:755px;top:60px;width:308px;height:470px;background:linear-gradient(160deg,#5a6068 0%,#2b2d33 55%,#17181c 100%);border-right:14px solid #e6e6e6;box-shadow:8px 8px 20px rgba(0,0,0,.6)}
.dots{position:absolute;left:92px;top:545px;display:flex;gap:4px}
.dots span{width:11px;height:11px;border-radius:50%;background:var(--white)}
.dots span:first-child{background:var(--purple)}
/* share rail */
.share{position:absolute;left:1162px;top:276px;width:38px}
.share span{display:block;width:38px;height:38px;margin-bottom:2px;background:var(--purple);color:var(--white);font-size:9px;line-height:38px;text-align:center}
/* author */
.author{position:absolute;left:0;top:686px;width:1200px;height:334px;background:linear-gradient(135deg,#55356a 0%,var(--purple-band) 50%,#3c2450 100%)}
.author-photo{position:absolute;left:127px;top:56px;width:226px;height:226px;border-radius:50%;border:3px solid #d8cfe0;background:radial-gradient(circle at 50% 40%,#e8d7b8 0%,#c9b59a 50%,#a99a8a 100%)}
.author h2{position:absolute;left:376px;top:72px;font-size:26px;font-weight:400;color:var(--white)}
.author p{position:absolute;left:376px;top:106px;width:700px;font-size:13.5px;line-height:23px;color:var(--white)}
.btn-ghost{position:absolute;height:34px;line-height:31px;border:1.5px solid;border-radius:17px;font-size:12.5px;text-align:center}
.author .btn-ghost{left:376px;top:231px;width:118px;color:var(--white);border-color:var(--white)}
/* resources */
.resources{position:absolute;left:0;top:1020px;width:1200px;height:439px}
.resources h2{position:absolute;left:94px;top:104px;font-size:26px;font-weight:400}
.resources p{position:absolute;left:94px;top:146px;width:478px;font-size:13px;line-height:23px;color:var(--grey-text);text-align:justify}
.resources .btn-ghost{left:94px;top:325px;width:113px;color:var(--purple);border-color:var(--purple)}
.video-frame{position:absolute;left:599px;top:80px;width:511px;height:293px;border:1px solid #ddd;padding:7px;box-shadow:0 0 4px rgba(0,0,0,.15);background:var(--white)}
.video{position:relative;width:100%;height:100%;background:linear-gradient(180deg,#4b5b78 0%,#2b2f48 55%,#3a1f3a 100%)}
.video svg{position:absolute;left:50%;top:50%;transform:translate(-50%,-50%)}
/* store */
.store{position:absolute;left:0;top:1459px;width:1200px;height:536px;background:var(--light)}
.section-title{position:absolute;left:0;width:1200px;text-align:center;font-size:26px;font-weight:400}
.store .section-title{top:70px}
.card{position:absolute;top:141px;width:242px;height:293px;box-shadow:0 1px 4px rgba(0,0,0,.25)}
.card-label{position:absolute;left:0;bottom:28px;width:100%;text-align:center;font-family:"Oswald",Impact,sans-serif;font-weight:500;font-size:28px;color:var(--white);text-shadow:0 1px 3px rgba(0,0,0,.7)}
/* newsletter */
.newsletter{position:absolute;left:0;top:1995px;width:1200px;height:124px;background:var(--purple-deep)}
.newsletter h3{position:absolute;left:154px;top:42px;font-size:26px;font-weight:400;color:var(--white)}
.email-field{position:absolute;left:419px;top:35px;width:490px;height:49px;background:var(--white);border-radius:3px;font-size:18px;line-height:49px;padding-left:16px;color:#333}
.sign-btn{position:absolute;left:922px;top:35px;width:135px;height:49px;background:#111;color:var(--white);font-size:18px;line-height:49px;text-align:center;border-radius:3px}
/* blog */
.blog{position:absolute;left:0;top:2119px;width:1200px;height:379px}
.blog .section-title{top:72px}
.post-img{position:absolute;top:152px;width:161px;height:142px}
.post h4{position:absolute;top:159px;font-size:14.5px;font-weight:400}
.post .date{position:absolute;top:184px;font-size:13px}
.post p{position:absolute;top:205px;width:285px;font-size:11px;line-height:16px;color:#555}
.post .more{position:absolute;top:275px;font-size:12px;color:var(--purple)}
/* footer */
.site-footer{position:absolute;left:0;top:2498px;width:1200px;height:319px;background:var(--footer);color:#ddd}
.footer-brand{position:absolute;left:92px;top:108px;font-family:"Roboto Slab",Georgia,serif;font-weight:700;font-size:28px;color:#eee}
.footer-col{position:absolute;top:56px;font-size:12px;line-height:22px}
.footer-col h5{font-size:14px;font-weight:400;margin-bottom:12px;color:#eee}
.footer-col ul{list-style:none}
.social-list{display:flex;gap:12px;font-size:13px;font-weight:600;color:#eee}
.rule{position:absolute;left:92px;top:220px;width:1020px;height:1px;background:#555}
.copyright{position:absolute;left:0;top:255px;width:1200px;text-align:center;font-size:12px}
</style>
</head>
<body>

<header class="site-header">
  <div class="brand">TAMSIN ROARK</div>
  <nav class="nav">
    <a class="active" href="#">HOME</a>
    <a style="left:548px" href="#">BOOKS</a>
    <a style="left:642px" href="#">RESOURCES</a>
    <a style="left:770px" href="#">STORE</a>
    <a style="left:860px" href="#">BLOG</a>
    <a style="left:942px" href="#">CONTACT US</a>
    <span class="cart">
      <svg width="18" height="16" viewBox="0 0 18 16"><path d="M1 2h3l2 8h9l2-6H5" fill="none" stroke="#6a1bb0" stroke-width="2"/><circle cx="7" cy="13.5" r="1.6" fill="#6a1bb0"/><circle cx="14" cy="13.5" r="1.6" fill="#6a1bb0"/></svg>: 0
    </span>
  </nav>
</header>

<section class="hero">
  <div class="hero-title">TAMSIN ROARK</div>
  <div class="hero-sub">CONSPIRACY NOVELS</div>
  <div class="hero-tag">Neque porro quisquam est qui ipsum</div>
  <div class="book-cover" role="img" aria-label="Book cover showing a cloaked heroine on a rocky dark landscape"></div>
  <div class="dots"><span></span><span></span><span></span></div>
</section>

<div class="share">
  <span>Hubbl</span><span>Chirra</span><span>Plexo</span><span>Workly</span><span>Pinora</span>
</div>

<section class="author">
  <div class="author-photo" role="img" aria-label="Portrait photo of the author"></div>
  <h2>AUTHOR</h2>
  <p>It is a long established fact that a reader will be distracted by the readable content of a page when looking at its layout. The point of using Lorem Ipsum is that it has a more-or-less normal distribution of letters, as opposed to using 'Content here, content here', making it look like readable English. Many desktop publishing packages and web page editors now use Lorem Ipsum as their default model text, and a search for 'lorem ipsum' will uncover many web sites still in their infancy.</p>
  <div class="btn-ghost">READ MORE »</div>
</section>

<section class="resources">
  <h2>RESOURCES</h2>
  <p>It is a long established fact that a reader will be distracted by the readable content of a page when looking at its layout. The point of using Lorem Ipsum is that it has a more-or-less normal distribution of letters, as opposed to using 'Content here, content here', making it look like readable English. Many desktop publishing packages and web page editors now use Lorem Ipsum as their default model text, and a search for 'lorem ipsum' will uncover many web sites still in their infancy.</p>
  <div class="btn-ghost">Read More »</div>
  <div class="video-frame">
    <div class="video" role="img" aria-label="Video trailer still of a reader sitting between tall library shelves">
      <svg width="64" height="64" viewBox="0 0 64 64"><circle cx="32" cy="32" r="31" fill="rgba(0,0,0,.55)"/><path d="M25 19l21 13-21 13z" fill="#fff"/></svg>
    </div>
  </div>
</section>

<section class="store">
  <h2 class="section-title">STORE</h2>
  <div class="card" style="left:92px;background:linear-gradient(160deg,#8a5a6a 0%,#5a3a45 50%,#3a2a30 100%)" role="img" aria-label="Book cover with autumn leaves scene"><div class="card-label">THRILLER</div></div>
  <div class="card" style="left:351px;background:linear-gradient(170deg,#4a3a36 0%,#2e2220 55%,#1a1212 100%)" role="img" aria-label="Book cover with a gothic doll figure"><div class="card-label">CONSPIRACY</div></div>
  <div class="card" style="left:610px;background:radial-gradient(circle at 50% 35%,#8a6a3a 0%,#2a1e14 45%,#0a0806 100%)" role="img" aria-label="Book cover with a candle on a skull"><div class="card-label">THRILLER</div></div>
  <div class="card" style="left:870px;background:radial-gradient(circle at 50% 50%,#3c5aa0 0%,#1e2e66 50%,#0d1433 100%)" role="img" aria-label="Book cover with an owl in a stone archway"><div class="card-label">SECRET AGENT</div></div>
</section>

<section class="newsletter">
  <h3>NEWSLETTER SIGN</h3>
  <div class="email-field">Email id</div>
  <div class="sign-btn">SIGN IN</div>
</section>

<section class="blog">
  <h2 class="section-title">LATEST BLOG</h2>
  <div class="post">
    <div class="post-img" style="left:96px;background:linear-gradient(150deg,#4a5a5a 0%,#2a3434 60%,#1a2020 100%)" role="img" aria-label="Photo of a woman in a dark dress in a forest"></div>
    <h4 style="left:272px">Nemo Enim Ipsam Volup</h4>
    <div class="date" style="left:272px">09-07-2017</div>
    <p style="left:272px">Lorem Ipsum has been the industry's standard dummy text ever since the 1500s, when an unknown printer took a galley of type and scrambled it to make a type specimen</p>
    <div class="more" style="left:272px">Read More &gt;&gt;</div>
  </div>
  <div class="post">
    <div class="post-img" style="left:633px;background:linear-gradient(150deg,#6a6a72 0%,#4a4650 55%,#2a2830 100%)" role="img" aria-label="Photo of a woman in a pale outfit"></div>
    <h4 style="left:811px">Nemo Enim Ipsam Volup</h4>
    <div class="date" style="left:811px">09-07-2017</div>
    <p style="left:811px">Lorem Ipsum has been the industry's standard dummy text ever since the 1500s, when an unknown printer took a galley of type and scrambled it to make a type specimen</p>
    <div class="more" style="left:811px">Read More &gt;&gt;</div>
  </div>
</section>

<footer class="site-footer">
  <div class="footer-brand">TAMSIN ROARK</div>
  <div class="footer-col" style="left:389px">
    <h5>QUICK LINKS</h5>
    <ul style="line-height:17px"><li>» Books</li><li>» Resources</li><li>» Store</li><li>» Blog</li><li>» Contact us</li></ul>
  </div>
  <div class="footer-col" style="left:644px">
    <h5>CONTACT US</h5>
    <ul><li>Address : 12 Harrow Lane, Eastgate</li><li>Bristol, BS4 7QL</li><li>Phone : 555-018-2247.</li><li>Email : hello@roarkbooks.test</li></ul>
  </div>
  <div class="footer-col" style="left:939px">
    <h5>FOLLOW US OUT THERE</h5>
    <div class="social-list"><span>Hubbl</span><span>Chirra</span><span>Workly</span><span>Plexo</span></div>
  </div>
  <div class="rule"></div>
  <div class="copyright">Copyright © 2017. All Rights Reserved</div>
</footer>

</body>
</html>
```